Crest of Morning Paddocks Business Cards with logo

Need a creative business card that pops. Colorful but professional. The attached logo should be included. We are a national horse racing partnership so we are in the equine business. Nothing cartoonlike or whimsical.

Target Market(s)

professionals - 40+

Contact Information for Business Card

Maren Dunleavy
Director of Operations
27 Ashbrook Lane
Middletown, MD. 21584

Phone (313) 555-0147

FX: (949) 555-0192

email: maren@cmpaddocks.example
cmpaddocks.example

Requirements
Must have
• All information above should be on the business card including the website address. Professional yet creative
Nice to have
• an attention grabbing design. not boring. exciting.
Should not have
• cartoon like - whimsical.

```html
<!DOCTYPE html>
<html lang="en">
<head>
<meta charset="utf-8">
<title>Crest of Morning Paddocks – Business Cards</title>
<link href="https://fonts.googleapis.com/css2?family=Cinzel:wght@700&family=Open+Sans:wght@400&display=swap" rel="stylesheet">
<style>
  :root {
    --navy: #2e3270;
    --gold: #bf922b;
    --white: #ffffff;
    --backdrop: #d4d4d4;
  }
  * { margin: 0; padding: 0; box-sizing: border-box; }
  html, body { width: 1200px; height: 866px; overflow: hidden; background: var(--backdrop); }
  .sheet {
    width: 1200px; height: 866px;
    display: flex; align-items: center; justify-content: center; gap: 40px;
  }
  .card {
    position: relative;
    width: 560px; height: 320px;
    background: var(--navy);
    overflow: hidden;
    box-shadow: 0 6px 14px rgba(0,0,0,0.25);
  }
  .card-art { position: absolute; inset: 0; }
  .contact-block {
    position: absolute;
    left: 290px; top: 150px; width: 240px;
    text-align: right;
  }
  .person-name {
    font-family: "Cinzel", serif; font-weight: 700;
    color: var(--gold); font-size: 21px; letter-spacing: 1px;
    text-align: left;
  }
  .person-title {
    font-family: "Open Sans", sans-serif;
    color: var(--white); font-size: 13px; letter-spacing: 0.5px;
    text-align: left; margin-top: 1px;
  }
  .contact-list { list-style: none; margin-top: 18px; }
  .contact-list li {
    font-family: "Open Sans", sans-serif;
    color: var(--white); font-size: 11.5px; line-height: 15px;
    display: flex; justify-content: flex-end; align-items: center; gap: 5px;
  }
  .contact-list .icon { width: 10px; height: 10px; flex: none; }
  .contact-list .address { padding-right: 15px; }
  .contact-list .address-first { margin-top: 4px; }
  .brand-mark {
    position: absolute; inset: 0;
    display: flex; flex-direction: column; align-items: center; justify-content: center; gap: 16px;
  }
  .brand-dot { width: 46px; height: 46px; border-radius: 50%; background: var(--gold); }
  .brand-name {
    font-family: "Cinzel", serif; font-weight: 700;
    color: var(--white); font-size: 20px; letter-spacing: 3px;
    text-align: center; line-height: 28px;
  }
</style>
</head>
<body>
<main class="sheet">
  <section class="card card-front">
    <svg class="card-art" width="560" height="320" viewBox="0 0 560 320">
      <path class="corner-band" d="M0 0 H330 L0 300 Z" fill="var(--gold)"/>
      <circle class="corner-disc" cx="190" cy="170" r="160" fill="var(--navy)"/>
      <rect class="trophy-illustration" x="105" y="55" width="180" height="215" rx="40"
            fill="var(--gold)" role="img" aria-label="Gold trophy cup illustration"/>
    </svg>
    <div class="contact-block">
      <h1 class="person-name">Maren Dunleavy</h1>
      <p class="person-title">Director of Operations</p>
      <ul class="contact-list">
        <li>(313) 555-0147
          <svg class="icon" viewBox="0 0 10 10"><path d="M1 3 Q5 0 9 3 L8 5 L6 4 L4 4 L2 5 Z M2 6 H8 V9 H2 Z" fill="var(--gold)"/></svg></li>
        <li>(949) 555-0192
          <svg class="icon" viewBox="0 0 10 10"><rect x="1" y="4" width="8" height="5" fill="var(--gold)"/><rect x="3" y="1" width="4" height="3" fill="var(--gold)"/></svg></li>
        <li>maren@cmpaddocks.example
          <svg class="icon" viewBox="0 0 10 10"><rect x="0.5" y="2" width="9" height="6" fill="var(--gold)"/><path d="M0.5 2 L5 5.5 L9.5 2" stroke="var(--navy)" fill="none"/></svg></li>
        <li>www.cmpaddocks.example
          <svg class="icon" viewBox="0 0 10 10"><circle cx="5" cy="5" r="4.5" fill="var(--gold)"/><path d="M0.5 5 H9.5 M5 0.5 V9.5" stroke="var(--navy)" stroke-width="0.8"/></svg></li>
        <li class="address address-first">27 Ashbrook Lane</li>
        <li class="address">Middletown, MD. 21584</li>
      </ul>
    </div>
  </section>

  <section class="card card-back">
    <div class="brand-mark">
      <span class="brand-dot"></span>
      <p class="brand-name">Crest of Morning<br>Paddocks</p>
    </div>
  </section>
</main>
</body>
</html>
```